Spring Savings Package for The Lodge at Harlan's Meadow Lodge

Design an email and elevator poster 11x7 that promotes Spring and our heated pools at The Lodge at Harlan's Meadow
Text-

Worried about the Spring Weather don't #IndoorWaterpark !

Ask about our Springtime Savings that comes with a Free Resort Beach Towel ($12 value).

Book by March 1st,2019
Stay Dates Now-May 23rd,2019

Phone number: 800.555.0192

Reserve Now! www (dot) lodgeatharlansmeadow (dot) com

Target Market(s)

Guest reserving Spring Break

Industry/Entity Type

Hospitality

Requirements
Must have
• text
• phone
• website
• Book Now
• Can change some of the text to make it more of a Sales piece
Nice to have
• Brand Colors

```html
<!DOCTYPE html>
<html lang="en">
<head>
<meta charset="utf-8">
<title>Spring Savings – The Lodge at Harlan's Meadow</title>
<link rel="stylesheet" href="https://fonts.googleapis.com/css2?family=Tinos:wght@400;700&family=Cherry+Swash&family=Archivo+Narrow:wght@700&display=swap">
<style>
  :root {
    --page: #7a7b79;
    --paper: #ffffff;
    --tan: #d6a060;
    --navy: #27306e;
    --body-grey: #555555;
    --panel-grey: #efefef;
    --teal: #4f7f88;
    --spring-bg: #fde8f4;
    --spring: #d8197c;
    --fall-bg: #fdf0c8;
    --fall: #d4a012;
    --summer-bg: #e6f4fd;
    --summer: #1a6fc4;
  }
  * { margin: 0; padding: 0; box-sizing: border-box; }
  html, body { width: 1200px; height: 2312px; overflow: hidden; background: var(--page); }
  body { position: relative; font-family: "Tinos", "Times New Roman", serif; }

  .email { position: absolute; left: 68px; top: 19px; width: 1089px; height: 2273px; background: var(--paper); overflow: hidden; }

  .masthead { position: absolute; left: 0; top: 0; width: 100%; height: 196px; }
  .brand { position: absolute; display: flex; align-items: center; gap: 14px; color: var(--navy); font-weight: 700; white-space: nowrap; }
  .brand-main { left: 28px; top: 74px; font-size: 32px; }
  .brand-sub { right: 30px; top: 74px; font-size: 32px; }
  .brand-mark { width: 22px; height: 22px; background: var(--tan); flex: none; }
  .brand-dot { width: 20px; height: 20px; border-radius: 50%; background: var(--fall); flex: none; }

  .nav { position: absolute; left: 0; top: 196px; width: 100%; height: 58px; background: var(--tan); }
  .nav span { position: absolute; top: 13px; transform: translateX(-50%); color: #fff; font-size: 26px; white-space: nowrap; }

  .hero { position: absolute; left: 0; top: 254px; width: 100%; height: 640px;
    background: linear-gradient(180deg, #b98a4e 0%, #7d9fb4 30%, #6fb7d6 60%, #7fd0e6 100%); }
  .hero-wave { position: absolute; left: 0; top: 740px; width: 1089px; height: 170px; }
  .badge { position: absolute; left: 827px; top: 698px; width: 224px; height: 224px; }
  .badge svg { display: block; }
  .badge-text { position: absolute; left: 0; top: 50px; width: 100%; text-align: center; color: #fff; font-size: 31px; line-height: 1.1; }
  .badge-text strong { display: block; font-size: 44px; font-weight: 400; margin-top: 4px; }

  .headline { position: absolute; left: 0; top: 945px; width: 100%; text-align: center; color: var(--navy); font-size: 35px; font-weight: 700; line-height: 46px; }
  .intro { position: absolute; left: 0; top: 1063px; width: 100%; text-align: center; color: var(--body-grey); font-size: 25px; line-height: 39px; }

  .offers { position: absolute; left: 0; top: 1257px; width: 100%; height: 530px; }
  .offer { position: absolute; top: 0; height: 530px; }
  .offer-spring { left: 0; width: 355px; background: var(--spring-bg); color: var(--spring); }
  .offer-fall { left: 360px; width: 356px; background: var(--fall-bg); color: var(--fall); }
  .offer-summer { left: 723px; width: 366px; background: var(--summer-bg); color: var(--summer); }
  .offer-title { font-family: "Cherry Swash", cursive; font-weight: 400; text-align: center; padding-top: 26px; line-height: 46px; font-size: 48px; }
  .offer-title span { display: block; font-size: 56px; line-height: 54px; }
  .offer-photo { position: absolute; left: 0; top: 143px; width: 100%; height: 252px; }
  .offer-spring .offer-photo { background: linear-gradient(180deg, #9fb89a, #e8d36a 45%, #9ed4e4); }
  .offer-fall .offer-photo { background: linear-gradient(180deg, #7fa7d9, #b78a52 40%, #78c5dc); }
  .offer-summer .offer-photo { background: linear-gradient(180deg, #d9d6d0, #e4e0dc 40%, #a9d3df); }
  .offer-save { position: absolute; left: 0; top: 402px; width: 100%; display: flex; justify-content: center; align-items: flex-start; gap: 8px;
    font-family: "Archivo Narrow", "Arial Narrow", sans-serif; font-weight: 700; }
  .offer-save .lead { font-size: 33px; line-height: 31px; text-align: center; padding-top: 20px; }
  .offer-save .rate { font-size: 78px; line-height: 86px; }
  .offer-save .rate sup { font-size: 40px; vertical-align: 30px; }

  .booking { position: absolute; left: 0; top: 1803px; width: 100%; height: 318px; background: var(--panel-grey); text-align: center; color: var(--navy); }
  .booking p { font-size: 31px; line-height: 52px; }
  .booking-lines { padding-top: 38px; }
  .reserve { position: absolute; left: 360px; top: 215px; width: 305px; height: 73px; background: var(--navy); color: #fff;
    font-size: 26px; font-weight: 700; line-height: 73px; text-align: center; }

  .footer { position: absolute; left: 0; top: 2121px; width: 100%; height: 152px; background: var(--tan); text-align: center; color: #fff; }
  .footer-url { padding-top: 32px; font-size: 29px; }
  .footer-copy { margin-top: 12px; font-size: 19px; }
</style>
</head>
<body>
<main class="email">
  <header class="masthead">
    <div class="brand brand-main"><span class="brand-mark"></span><span>The Lodge at Harlan's Meadow</span></div>
    <div class="brand brand-sub"><span>Lantern Hollow</span><span class="brand-dot"></span></div>
  </header>

  <nav class="nav">
    <span style="left:146px">GUEST ROOMS</span>
    <span style="left:402px">WATERPARK</span>
    <span style="left:637px">DISCOUNTS</span>
    <span style="left:918px">RECREATION</span>
  </nav>

  <div class="hero" role="img" aria-label="Smiling kids on a big inflatable float in the outdoor pool, lodge buildings and waterslides behind"></div>
  <svg class="hero-wave" viewBox="0 0 1089 170" aria-hidden="true">
    <path d="M0 68 C 200 40, 420 20, 640 70 S 960 130, 1089 40 L1089 170 L0 170 Z" fill="var(--teal)"/>
    <path d="M0 84 C 200 56, 420 40, 640 90 S 960 150, 1089 62 L1089 170 L0 170 Z" fill="#ffffff"/>
  </svg>

  <div class="badge">
    <svg viewBox="0 0 232 232" width="224" height="224" aria-hidden="true">
      <g fill="#ffffff" transform="translate(116 116)">
        <rect x="-88" y="-88" width="176" height="176"/>
        <rect x="-88" y="-88" width="176" height="176" transform="rotate(15)"/>
        <rect x="-88" y="-88" width="176" height="176" transform="rotate(30)"/>
        <rect x="-88" y="-88" width="176" height="176" transform="rotate(45)"/>
        <rect x="-88" y="-88" width="176" height="176" transform="rotate(60)"/>
        <rect x="-88" y="-88" width="176" height="176" transform="rotate(75)"/>
      </g>
      <g fill="var(--tan)" transform="translate(116 116)">
        <rect x="-82" y="-82" width="164" height="164"/>
        <rect x="-82" y="-82" width="164" height="164" transform="rotate(15)"/>
        <rect x="-82" y="-82" width="164" height="164" transform="rotate(30)"/>
        <rect x="-82" y="-82" width="164" height="164" transform="rotate(45)"/>
        <rect x="-82" y="-82" width="164" height="164" transform="rotate(60)"/>
        <rect x="-82" y="-82" width="164" height="164" transform="rotate(75)"/>
      </g>
    </svg>
    <div class="badge-text">SUMMER<br>OFFER<strong>30%</strong></div>
  </div>

  <h1 class="headline">WORRIED ABOUT THE WEATHER<br>DON'T #HEATEDPOOLS !</h1>
  <p class="intro">Ask about our Springtime Savings that comes with a<br>Free Quillbrook Waterpark Resort Beach Towel ($12 value).<br>PLUS! A Mountain Breakfast at<br>Nana's Table is included with all stays.</p>

  <section class="offers">
    <div class="offer offer-spring">
      <h2 class="offer-title">Spring<span>Savings</span></h2>
      <div class="offer-photo" role="img" aria-label="Girl splashing out of a yellow slide into the indoor pool"></div>
      <div class="offer-save"><span class="lead">Save<br>up to</span><span class="rate">20<sup>%</sup></span></div>
    </div>
    <div class="offer offer-fall">
      <h2 class="offer-title">Fall<span>Savings</span></h2>
      <div class="offer-photo" role="img" aria-label="Kids on an inflatable float in the outdoor pool"></div>
      <div class="offer-save"><span class="lead">Save<br>up to</span><span class="rate">30<sup>%</sup></span></div>
    </div>
    <div class="offer offer-summer">
      <h2 class="offer-title">Summer<span>Savings</span></h2>
      <div class="offer-photo" role="img" aria-label="Children playing in the indoor splash area"></div>
      <div class="offer-save"><span class="lead">Save<br>up to</span><span class="rate">35<sup>%</sup></span></div>
    </div>
  </section>

  <section class="booking">
    <div class="booking-lines">
      <p>Book by March 1st,2019</p>
      <p>Stay Dates Now-May 23rd,2019</p>
      <p>Phone number: 800.555.0192</p>
    </div>
    <div class="reserve">RESERVE NOW!</div>
  </section>

  <footer class="footer">
    <p class="footer-url">www.lodgeatharlansmeadow.com</p>
    <p class="footer-copy">Copyright @ 2019 lodgeatharlansmeadow.com</p>
  </footer>
</main>
</body>
</html>
```